Our landing page needs to be updated - 1 panel only - SEE NEW MESSAGE AND MOCK UP CONCEPT screenshot

We require the top page of our landing page redesigned to better convey our product offering.

The application is an email marketing platform offering pre-designed and ready-to-use email templates.
The landing page should (a) visually convey our product proposition - ie - display a sample of the email templates (resources provided) and also (b) in copy format explain our product proposition.

There are SIX categories for the templates - on the attached resources these are explained.
You should visit KOVRELL.COM - to see more information (and how bad our current landing page is)

It should be clear there are six categories - their headings are:

1. Message someone
2. Share important information
3. Promote Deals and Special Offers
4. Announce Events
5. Broadcast Newsletters
6. Advertise your Products or Services

These headings are only intended to explain why there are different template designs - they are secondary information

The copy hierarchy is:

Main sell
"Ready-To-Use Email Templates"

Supporting sell

"Insert your images and links then send. It’s that quick and easy.
Beautiful emails deliver better results."

Last sell checklist

"Free image library
300 plus designs
Email analytics"

The images (cropped as required) of our templates are the heroes - the copy should be supporting.

Purple is our primary brand colour

Logo is also provided

At kovrell.com we like "Sign In" being held in a box

Our colour pallet is attached

NB - at Kovrell.com - all panels will remain on the Landing page - other than the top panel - ie - above the fold - this is the one we require redesigning because the image of a female at a keyboard does not convey our product offering.

Button shapes should be consistent with those already on Kovrell.com

Our Font family is LATO

Industry/Entity Type

Marketing

Number of Pages Required

1 page

Requirements
Must have
• Our font family - LATO and our colour pallett
• Our sample email templates
• Top Right - navigation links - "Pricing Create Account Sign In"

```html
<!DOCTYPE html>
<html lang="en">
<head>
<meta charset="utf-8">
<title>Kovrell – Ready-to-use email templates</title>
<link href="https://fonts.googleapis.com/css2?family=Lato:wght@400;700;900&display=swap" rel="stylesheet">
<style>
:root{
  --purple:#93319b;
  --purple-light:#a13eaa;
  --blue:#00aeef;
  --blue-dark:#0a8fc8;
  --page:#f5f6fa;
  --ink:#333a4a;
  --muted:#9aa3b5;
  --line:#dde1ea;
  --white:#ffffff;
  --accent:#e5245e;
  --teal:#1fb3a6;
}
*{box-sizing:border-box;margin:0;padding:0}
html,body{width:959px;height:1200px;overflow:hidden}
body{font-family:"Lato",sans-serif;background:var(--page);position:relative}
.hero{position:absolute;left:0;top:0;width:959px;height:580px}
.hero-bg{position:absolute;left:0;top:0}
.nav{position:absolute;left:187px;right:188px;top:8px;height:20px;display:flex;align-items:center;color:var(--white)}
.brand{font-weight:900;font-size:14px;letter-spacing:-.2px}
.nav-links{margin-left:auto;display:flex;align-items:center;font-size:7px;font-weight:700}
.nav-links a{color:var(--white);text-decoration:none;margin-left:29px}
.nav-links .signin{border:1px solid rgba(255,255,255,.8);border-radius:9px;padding:4px 9px;margin-left:21px}
.mock{position:absolute;left:287px;top:125px;width:385px;height:235px;background:var(--white);border-radius:3px;box-shadow:0 10px 30px rgba(60,0,70,.25);overflow:hidden}
.mock-band{position:absolute;left:0;top:0;width:385px;height:60px}
.mock-email{position:absolute;left:51px;top:45px;width:284px;height:190px;background:var(--white);box-shadow:0 0 10px rgba(0,0,0,.06)}
.mock-image{height:120px;background:var(--blue);display:flex;align-items:center;justify-content:center}
.mock-icon{display:block}
.mock-line{position:absolute;left:50%;transform:translateX(-50%);height:4px;border-radius:2px;background:#e6e9ef}
.hero-title{position:absolute;left:0;right:0;top:389px;text-align:center;color:var(--white);font-size:16px;font-weight:700}
.btn{position:absolute;left:430px;top:430px;width:99px;height:24px;border-radius:12px;background:var(--blue);color:var(--white);font-size:7px;font-weight:700;display:flex;align-items:center;justify-content:center}
.section-title{position:absolute;left:0;right:0;top:676px;text-align:center;color:var(--ink);font-size:15px;font-weight:700}
.section-sub{position:absolute;left:0;right:0;top:702px;text-align:center;color:var(--muted);font-size:7px;font-weight:700}
.tabs{position:absolute;left:187px;top:760px;width:584px;height:25px;border:1px solid var(--line);border-radius:13px;font-size:6.5px;color:var(--ink)}
.tab{position:absolute;top:0;height:23px;line-height:23px;transform:translateX(-50%);white-space:nowrap}
.tab.active{left:0;transform:none;top:-1px;height:25px;line-height:25px;width:86px;text-align:center;background:var(--purple);color:var(--white);font-weight:700;border-radius:13px}
.card{position:absolute;width:135px;height:135px;background:#eef0f4;border:1px solid var(--line);overflow:hidden}
.card.plain{background:var(--white)}
.sheet{position:absolute;left:14px;top:6px;width:107px;height:140px;background:var(--white)}
.logo-text{text-align:center;font-size:6px;color:var(--ink);margin-top:7px}
.photo{margin:5px 3px 0;height:58px}
.card-heading{text-align:center;font-size:4.5px;font-weight:700;color:var(--ink);margin-top:3px}
.bar{height:2px;background:#d6d9e0;margin:3px 8px 0}
.cta{width:24px;height:4px;margin:4px auto 0;background:var(--accent)}
</style>
</head>
<body>
<section class="hero">
  <svg class="hero-bg" width="959" height="580" viewBox="0 0 959 580" aria-hidden="true">
    <defs>
      <linearGradient id="heroGrad" x1="0" y1="0" x2="1" y2="1">
        <stop offset="0" stop-color="#86278f"/>
        <stop offset="1" stop-color="#9a35a1"/>
      </linearGradient>
    </defs>
    <path d="M0 0H959V496L480 578L0 496Z" fill="url(#heroGrad)"/>
    <path d="M480 578 C620 540 760 470 840 380 C900 300 940 180 900 60 L959 60 V496 Z" fill="#a13eaa" opacity=".35"/>
  </svg>
  <nav class="nav">
    <div class="brand">Kovrell</div>
    <div class="nav-links">
      <a href="#">Pricing</a>
      <a href="#">Free Trial</a>
      <a href="#" class="signin">Sign in</a>
    </div>
  </nav>
  <div class="mock">
    <svg class="mock-band" viewBox="0 0 385 60" aria-hidden="true">
      <path d="M0 0H385V47L192 28L0 47Z" fill="#f4f5f8"/>
    </svg>
    <div class="mock-email">
      <div class="mock-image">
        <svg class="mock-icon" width="40" height="28" viewBox="0 0 40 28" aria-hidden="true">
          <circle cx="7" cy="5" r="3" fill="var(--blue-dark)"/>
          <path d="M0 26L10 12L17 20L25 8L38 26Z" fill="var(--blue-dark)"/>
        </svg>
      </div>
      <div class="mock-line" style="top:150px;width:60px"></div>
      <div class="mock-line" style="top:160px;width:100px"></div>
    </div>
  </div>
  <h1 class="hero-title">Ready-to-use email templates</h1>
  <div class="btn">Get Started</div>
</section>

<h2 class="section-title">Our email templates</h2>
<p class="section-sub">Professionally designed, responsive, mobile-ready templates.</p>

<div class="tabs">
  <div class="tab active">Message someone</div>
  <div class="tab" style="left:143px">Share information</div>
  <div class="tab" style="left:243px">Promote &amp; Special Offers</div>
  <div class="tab" style="left:343px">Announce Events</div>
  <div class="tab" style="left:443px">Broadcast Newsletters</div>
  <div class="tab" style="left:542px">Advertise Services</div>
</div>

<div class="card" style="left:187px;top:815px"><div class="sheet"><div class="logo-text">Your Logo</div><div class="photo" role="img" aria-label="Photo of a knitted blanket and dried flowers" style="height:70px;background:linear-gradient(#8a8d92,#5a5d63)"></div><div style="margin:0 3px;height:40px;background:#3b3d44;padding-top:5px"><div class="card-heading" style="color:#fff;margin:0">YOUR HEADING TO GO HERE</div></div></div></div>
<div class="card plain" style="left:338px;top:815px"><div class="sheet"><div class="photo" role="img" aria-label="Photo of a grey interior" style="height:26px;background:linear-gradient(#9aa0a6,#5f6368)"></div><div class="logo-text">YOUR LOGO</div><div class="bar"></div><div class="bar"></div><div class="bar"></div><div class="bar"></div><div class="bar"></div></div></div>
<div class="card plain" style="left:487px;top:815px"><div class="sheet"><div class="logo-text">Company Name</div><div class="photo" role="img" aria-label="Photos of people working with a promotion layout" style="height:105px;background:linear-gradient(#5b7fa8 0,#5b7fa8 30%,#f4a68a 30%,#f4a68a 65%,#6fd0c3 65%)"></div></div></div>
<div class="card" style="left:637px;top:815px"><div class="sheet"><div class="logo-text">YOUR LOGO</div><div class="bar"></div><div class="bar"></div><div class="photo" role="img" aria-label="Photo of a man in sunglasses" style="height:40px;background:linear-gradient(#8fb1b8,#4d6a70)"></div><div class="card-heading">YOUR HEADING TO GO HERE</div><div class="bar"></div><div class="cta"></div></div></div>

<div class="card" style="left:187px;top:965px"><div class="sheet"><div class="logo-text">YOUR LOGO</div><div style="margin:5px 3px 0;height:20px;background:#1c5a7a;padding-top:4px"><div class="card-heading" style="color:#fff;margin:0;font-size:5px;font-weight:400">YOUR WINNING HEADING</div></div><div class="photo" role="img" aria-label="Photo of a laptop on a desk" style="margin-top:0;height:60px;background:linear-gradient(#c89560,#6b5a4a)"></div><div class="bar"></div><div class="bar"></div></div></div>
<div class="card" style="left:338px;top:965px"><div class="sheet"><div class="logo-text" style="color:var(--blue)">your logo</div><div class="photo" role="img" aria-label="Colourful abstract pattern" style="height:28px;background:linear-gradient(90deg,#00c2e8,#35d0f0)"></div><div class="bar"></div><div class="bar"></div><div class="bar"></div><div class="bar"></div><div class="bar"></div><div class="cta"></div></div></div>
<div class="card plain" style="left:487px;top:965px"><div class="sheet"><div class="logo-text">YOUR LOGO</div><div class="photo" role="img" aria-label="Portrait photos" style="height:34px;background:linear-gradient(#d9cbbd,#a38d7a)"></div><div class="bar"></div><div class="bar"></div><div class="bar"></div><div class="bar"></div><div class="bar"></div></div></div>
<div class="card" style="left:637px;top:965px;background:#dfeeed"><div class="sheet"><div class="logo-text" style="color:#1a9c9c">Your LOGO</div><div class="bar"></div><div class="bar"></div><div class="photo" role="img" aria-label="Photo of flowers on a teal shelf" style="height:46px;background:linear-gradient(#2fb6ae,#1c7f7a)"></div><div class="card-heading" style="color:#1a9c9c">YOUR HEADING TO GO HERE</div><div class="bar"></div><div class="cta" style="background:var(--teal)"></div></div></div>
</body>
</html>
```